plumbing & gas fitting business card design

We need a business card design for a plumbing & gas fitting company. The company covers commercial, domestic and maintenance work. We would like a modern design communicating efficiency and sophistication. preferred colours would include (red grey & black) or (green grey & black). Please DO NOT include any water droplets.

Industry/Entity Type

Business

Contact Information for Business Card

Vortig Plumbing & Gas, Commercial Domestic & Maintenance, licence no. 617394K, ABN 47215830962, Phone 0417382956, Email vortigplumbingandgas@corvanet.com

```html
<!DOCTYPE html>
<html lang="en">
<head>
<meta charset="utf-8">
<title>Vortig Plumbing &amp; Gas – Business Card</title>
<link rel="stylesheet" href="https://fonts.googleapis.com/css2?family=Open+Sans:wght@400;700&display=swap">
<style>
  :root {
    --card-black: #000000;
    --edge-grey: #6e6e6e;
    --deep-red: #4a140e;
    --accent-orange: #ee3b24;
    --text-red: #ec1c24;
    --page-bg: #ffffff;
  }
  html, body {
    margin: 0;
    padding: 0;
    width: 1200px;
    height: 692px;
    overflow: hidden;
    background: var(--page-bg);
  }
  .business-card {
    position: relative;
    width: 1200px;
    height: 692px;
    overflow: hidden;
    background: var(--card-black);
    font-family: "Open Sans", sans-serif;
    color: var(--text-red);
  }
  .accent-field {
    position: absolute;
    top: 0;
    right: 0;
    width: 560px;
    height: 692px;
    background: linear-gradient(90deg,
      var(--card-black) 0%,
      var(--deep-red) 45%,
      var(--accent-orange) 88%);
  }
  .card-text {
    position: absolute;
    margin: 0;
    white-space: nowrap;
    line-height: 1;
  }
  .licence-line {
    left: 66px;
    top: 72px;
    font-size: 29px;
    font-weight: 700;
  }
  .company-name {
    left: 157px;
    top: 246px;
    font-size: 47px;
    font-weight: 700;
  }
  .service-line {
    left: 78px;
    top: 328px;
    font-size: 40px;
    font-weight: 700;
  }
  .phone-line {
    left: 64px;
    top: 528px;
    font-size: 33px;
    font-weight: 400;
  }
  .email-line {
    left: 64px;
    top: 578px;
    font-size: 30px;
    font-weight: 400;
  }
</style>
</head>
<body>
  <div class="business-card">
    <div class="accent-field" role="img" aria-label="Decorative red-orange jagged shard graphic along the right edge"></div>

    <p class="card-text licence-line">licence no. 617394K, ABN 47215830962</p>
    <h1 class="card-text company-name">Vortig Plumbing &amp; Gas,</h1>
    <p class="card-text service-line">Commercial Domestic &amp; Maintenance</p>
    <p class="card-text phone-line">Phone: 0417382956</p>
    <p class="card-text email-line">Email: vortigplumbingandgas@corvanet.com</p>
  </div>
</body>
</html>
```